Poetry Book Cover Design Project

Looking for a minimalistic book cover design for a collection of poems. The book title is "Where The Lanterns Drift Slowly Apart". There are three parts to the book. First covers poetry in the theme of Rage. Second love and desire. The third is strange poems. Essentially the sections are "Rage", "Desire" and the "Strange". The reason for the title "Where The Lanterns Drift Slowly Apart" is as if someone is writing these till life changes towards the intended outcome as felt in each poem. I want to have the author's name "Nuwanthi Karunasekera" at the bottom. Ilustration attached.
- Minimalistic

```html
<!DOCTYPE html>
<html lang="en">
<head>
<meta charset="UTF-8">
<title>Where The Lanterns Drift Slowly Apart — Book Cover</title>
<link href="https://fonts.googleapis.com/css2?family=Playfair+Display:wght@900&family=Montserrat:wght@400;700&display=swap" rel="stylesheet">
<style>
  :root {
    --backdrop: #e9e9e9;
    --cover-paper: #fbfbfa;
    --ink: #151515;
    --plum: #7b2a66;
    --indigo: #2c3f86;
    --ocean: #1f6fa6;
    --lagoon: #1c9aa6;
    --leaf: #2fa563;
    --teal: #2a9d8f;
  }
  html, body {
    margin: 0;
    padding: 0;
    width: 1200px;
    height: 1200px;
    overflow: hidden;
    background: var(--backdrop);
  }
  .canvas {
    width: 1200px;
    height: 1200px;
    display: flex;
    align-items: center;
    justify-content: center;
  }
  .book-cover {
    position: relative;
    width: 780px;
    height: 1160px;
    background: var(--cover-paper);
    box-sizing: border-box;
  }
  .book-title {
    position: absolute;
    top: 70px;
    right: 56px;
    margin: 0;
    font-family: "Playfair Display", Georgia, serif;
    font-weight: 900;
    font-size: 150px;
    line-height: 0.93;
    letter-spacing: -0.01em;
    text-align: right;
    background: linear-gradient(165deg,
      var(--plum) 0%,
      var(--indigo) 22%,
      var(--ocean) 42%,
      var(--leaf) 58%,
      var(--lagoon) 72%,
      var(--teal) 100%);
    -webkit-background-clip: text;
    background-clip: text;
    color: transparent;
    -webkit-text-fill-color: transparent;
  }
  .book-title .title-line {
    display: block;
  }
  .series-label {
    position: absolute;
    top: 530px;
    left: 92px;
    margin: 0;
    font-family: "Montserrat", Arial, sans-serif;
    font-size: 25px;
    line-height: 1.2;
    letter-spacing: 0.04em;
    text-transform: uppercase;
    color: var(--ink);
    text-align: right;
  }
  .series-label .series-label-strong {
    font-weight: 700;
  }
  .author-name {
    position: absolute;
    right: 58px;
    bottom: 70px;
    margin: 0;
    font-family: "Montserrat", Arial, sans-serif;
    font-weight: 700;
    font-size: 36px;
    line-height: 1.3;
    letter-spacing: 0.08em;
    text-transform: uppercase;
    text-align: right;
    color: var(--ink);
  }
  .author-name span {
    display: block;
  }
</style>
</head>
<body>
  <main class="canvas">
    <article class="book-cover">
      <h1 class="book-title">
        <span class="title-line">where</span>
        <span class="title-line">the</span>
        <span class="title-line">lanterns</span>
        <span class="title-line">drift</span>
        <span class="title-line">slowly</span>
        <span class="title-line">apart.</span>
      </h1>
      <p class="series-label">Collection<br>of <span class="series-label-strong">Poems</span></p>
      <p class="author-name"><span>Nuwanthi</span><span>Karunasekera</span></p>
    </article>
  </main>
</body>
</html>
```